New Alcoholic Spiked Seltzer Line

We need a can design for a line of low calorie alcoholic seltzer. This product is a sparkling water and vodka drink with no sugar added in a slim 12 oz can.

This is a lighter, healthier, alternative to the sugary ready-to-drinks on the market. The product contains only 3 ingredients: Vodka, Water and Natural Flavors. It has only 100 calories but still has 5% alcohol, so you don't need to sacrifice alcohol to cut calories.

This product also does not contain any preservatives.

We want this design to communicate the following objectives to the consumer and in this order:

1. Appetizing product
2.Low calorie
3.Communicate the type of beverage (Spiked Seltzer)

The brand name of the product is VELKA.

The flavor of the product needed to be used for the design is Mango-Orange.

Comparable products are:

www.brisavelfizz.example/
https://www.tarnowbubble.example
https://quellrind.example/

The designs should not infringe or copy the creative directions of the products mentionned above. They are only given so that you can better understand the type of product we are developing.

Target Market(s)

Young Professional women between the ages of 25 and 44

Industry/Entity Type

Product

Colors

Designer to choose colors to be used in the design.

Requirements
Must have
• Design extendibility, meaning it can be adapted for other flavors.
• This is a new category in the market we are targeting, so consumers must easily be able to identify what type of product this is.

```html
<!DOCTYPE html>
<html lang="en">
<head>
<meta charset="utf-8">
<title>VELKA Spiked Seltzer – Mango-Orange can label</title>
<link rel="stylesheet" href="https://fonts.googleapis.com/css2?family=Jost:wght@300;400&display=swap">
<style>
  :root {
    --stage: #e4e3e6;
    --label-white: #f7f7f5;
    --ink: #111111;
    --wine: #8e1b24;
    --navy: #1f2d6b;
    --sun: #f2be1a;
    --sky: #0a86d0;
    --signal-red: #b3121d;
    --mango: #e9a02a;
    --citrus: #f2a11c;
  }
  * { box-sizing: border-box; margin: 0; padding: 0; }
  html, body {
    width: 1200px; height: 849px; overflow: hidden;
    background: var(--stage);
    font-family: "Jost", "Futura", sans-serif;
  }
  .label-wrap {
    position: absolute; left: 60px; top: 124px;
    width: 1080px; height: 600px;
    background: var(--label-white);
    overflow: hidden;
  }
  .edge-stripe { position: absolute; top: 0; width: 10px; height: 100%; background: var(--signal-red); }
  .edge-stripe--left { left: 0; }
  .edge-stripe--right { right: 0; height: 240px; }

  .brand-name {
    position: absolute; left: 30px; top: -14px;
    font-size: 172px; font-weight: 300; letter-spacing: 6px;
    color: var(--ink); line-height: 1; white-space: nowrap;
  }
  .brand-name--vertical {
    left: 470px; top: 236px;
    font-size: 100px; letter-spacing: 4px;
    writing-mode: vertical-rl; transform: rotate(180deg);
  }

  .product-type {
    position: absolute; left: 40px; top: 214px;
    font-size: 48px; font-weight: 400; line-height: 0.9;
    color: var(--wine);
  }
  .can-size {
    position: absolute; left: 286px; top: 214px;
    font-size: 68px; font-weight: 300; color: var(--navy); line-height: 1;
    white-space: nowrap;
  }
  .ring {
    position: absolute; border-radius: 50%;
    border: 9px solid var(--ink);
    display: flex; align-items: center; justify-content: center;
    text-align: center; overflow: hidden;
  }
  .ring--abv { left: 30px; top: 350px; width: 200px; height: 200px; }
  .abv-text { font-size: 42px; line-height: 0.95; color: var(--navy); font-weight: 400; }

  .calorie-block {
    position: absolute; left: 250px; top: 400px;
    width: 200px; height: 200px; background: var(--sun);
    padding: 20px 14px; font-size: 38px; line-height: 1; color: var(--navy);
  }

  .ring--mango { left: 600px; top: 26px; width: 200px; height: 200px; }
  .ring--orange { left: 600px; top: 310px; width: 200px; height: 200px; }
  .fruit-photo { width: 100%; height: 100%; }
  .fruit-photo--mango { background: radial-gradient(circle at 45% 45%, #f2c53a 0%, var(--mango) 35%, #d3542a 62%, var(--label-white) 64%); }
  .fruit-photo--orange { background: radial-gradient(circle at 50% 55%, #f9d48a 0%, var(--citrus) 40%, #e07a10 60%, var(--label-white) 62%); }

  .vertical-type {
    position: absolute; writing-mode: vertical-rl; transform: rotate(180deg);
    line-height: 0.9; white-space: nowrap;
  }
  .vertical-type--type { left: 816px; top: 430px; font-size: 36px; color: var(--wine); }
  .vertical-type--low-cal { left: 886px; top: 270px; font-size: 54px; font-weight: 300; color: var(--navy); }

  .ring--ingredients { left: 848px; top: 14px; width: 216px; height: 216px; }
  .ingredients {
    color: var(--wine); font-size: 30px; line-height: 0.9; text-align: center;
    width: 100%; padding: 0 22px;
  }
  .ingredients small { display: block; font-size: 17px; margin-top: 4px; white-space: nowrap; }

  .flavor-panel {
    position: absolute; left: 952px; top: 240px;
    width: 118px; height: 360px; background: var(--sky);
    display: flex; align-items: center; justify-content: center;
  }
  .flavor-name {
    writing-mode: vertical-rl; transform: rotate(180deg);
    font-size: 50px; font-weight: 400; color: var(--sun); line-height: 1;
    white-space: nowrap;
  }
</style>
</head>
<body>
  <main class="label-wrap">
    <div class="edge-stripe edge-stripe--left"></div>
    <div class="edge-stripe edge-stripe--right"></div>

    <div class="brand-name">VELKA</div>
    <div class="product-type">Spiked<br>Seltzer</div>
    <div class="can-size">12 oz</div>

    <div class="ring ring--abv"><p class="abv-text">5%<br>alcohol</p></div>
    <div class="calorie-block">100<br>calories</div>

    <div class="brand-name brand-name--vertical">VELKA</div>

    <div class="ring ring--mango">
      <div class="fruit-photo fruit-photo--mango" role="img" aria-label="Photo of a ripe mango with leaves and cut slices"></div>
    </div>
    <div class="ring ring--orange">
      <div class="fruit-photo fruit-photo--orange" role="img" aria-label="Photo of halved oranges with leaves"></div>
    </div>

    <div class="vertical-type vertical-type--type">Spiked<br>Seltzer</div>
    <div class="vertical-type vertical-type--low-cal">Low calorie</div>

    <div class="ring ring--ingredients">
      <p class="ingredients">Vodka<br>Water<small>Natural Flavors</small></p>
    </div>

    <div class="flavor-panel"><span class="flavor-name">Mango-Orange</span></div>
  </main>
</body>
</html>
```